Marlowe Tessin Real Estate Business Cards
Professional
Marlowe Tessin
Broker
782 W. Larkspur Ave, Suite 315
Cedar Grove, CA 91422
marlowe@marlowetessinrealestate.com
www.marlowetessinrealestate.com
These comments may or may not be included on the back of the card...
Menu of Services-
Investor Services
1% Listings for Flips
Rehab Management
Auction Services
Bidding
Tax & Title Review
Daily Auction Lists
Property Management Services
Leasing
Maintenance
Evictions
Real Estate Services
Buyers/Sellers
REO Specialists
BPO's
Notary
I'm open to ideas on what to have on either side. I'd like to have my picture and my logo on the card and it may or may not be on the same side. I'm also open to adding comments about services I offer (which I included above) but not sure if it works or not.
EPS Version of the logo
AI Version of the logo
JPG Version of the logo
GIF Version of the logo
My Headshot 1
My Headshot 2

```html
<!DOCTYPE html>
<html lang="en">
<head>
<meta charset="utf-8">
<title>Marlowe Tessin Real Estate Business Cards</title>
<link href="https://fonts.googleapis.com/css2?family=Montserrat:wght@400;600;700&family=Open+Sans:wght@400;600&display=swap" rel="stylesheet">
<style>
  :root {
    --bg: #e9eaea;
    --card-white: #ffffff;
    --teal: #2fb3c0;
    --teal-dark: #1d96a3;
    --teal-light: #d9f3f5;
    --ink: #4a4a4a;
    --ink-soft: #6b6b6b;
    --white: #ffffff;
  }
  * { box-sizing: border-box; margin: 0; padding: 0; }
  html, body { width: 1200px; height: 893px; overflow: hidden; }
  body {
    background: var(--bg);
    font-family: "Open Sans", Arial, sans-serif;
    color: var(--ink);
    position: relative;
  }
  .card {
    position: absolute;
    top: 300px;
    width: 500px;
    height: 286px;
    box-shadow: 0 6px 18px rgba(0,0,0,0.18);
    overflow: hidden;
  }

  /* Front */
  .card-front { left: 70px; background: var(--card-white); }
  .front-accent {
    position: absolute; left: 0; top: 0; width: 14px; height: 100%;
    background: var(--teal);
  }
  .front-corner { position: absolute; left: 0; bottom: 0; }
  .backdrop-art {
    position: absolute; right: 0; top: 70px; width: 150px; height: 190px;
    background: linear-gradient(180deg, rgba(47,179,192,0.10), rgba(47,179,192,0.02));
  }
  .headshot {
    position: absolute; left: 44px; top: 48px; width: 92px; height: 112px;
    background: linear-gradient(160deg, #8a6a5a 0%, #3b2c28 100%);
    border: 3px solid var(--white);
    box-shadow: 0 0 0 2px var(--teal);
  }
  .brand {
    position: absolute; left: 190px; top: 40px; width: 280px; text-align: center;
  }
  .brand-name, .brand-tag {
    font-family: "Montserrat", Arial, sans-serif;
    font-weight: 600;
    font-size: 24px;
    letter-spacing: 1px;
    color: var(--teal-dark);
    text-transform: uppercase;
    line-height: 1.2;
  }
  .agent {
    position: absolute; right: 40px; top: 130px; text-align: right;
  }
  .agent-name {
    font-family: "Montserrat", Arial, sans-serif;
    font-weight: 700; font-size: 21px; color: var(--ink);
  }
  .agent-title {
    font-family: "Montserrat", Arial, sans-serif;
    font-weight: 400; font-size: 17px; color: var(--teal-dark);
  }
  .contact {
    position: absolute; left: 44px; top: 178px; list-style: none;
    font-size: 10.5px; line-height: 15px; color: var(--ink-soft);
  }
  .contact li { display: flex; align-items: flex-start; gap: 6px; }
  .contact svg { width: 10px; height: 10px; flex: none; margin-top: 2.5px; }

  /* Back */
  .card-back {
    left: 630px;
    background: linear-gradient(160deg, var(--teal-light) 0%, #7fd3dc 40%, var(--teal) 100%);
  }
  .menu-title {
    position: absolute; top: 38px; width: 100%; text-align: center;
    font-family: "Montserrat", Arial, sans-serif;
    font-weight: 600; font-size: 24px; color: var(--ink); letter-spacing: 0.5px;
  }
  .services {
    position: absolute; top: 92px; left: 56px; right: 40px;
    display: grid; grid-template-columns: 1fr 1fr; column-gap: 40px; row-gap: 16px;
  }
  .service h3 {
    font-family: "Montserrat", Arial, sans-serif;
    font-weight: 700; font-size: 12.5px; color: var(--ink); margin-bottom: 2px;
  }
  .service ul { list-style: none; font-size: 12px; line-height: 15px; color: var(--white); }
</style>
</head>
<body>
  <section class="card card-front" aria-label="Business card front">
    <div class="front-accent"></div>
    <svg class="front-corner" width="40" height="24" viewBox="0 0 40 24" aria-hidden="true">
      <path d="M0 24 L0 4 Q20 14 40 24 Z" fill="var(--teal)"/>
    </svg>
    <div class="backdrop-art" role="img" aria-label="Faint city building backdrop"></div>
    <div class="headshot" role="img" aria-label="Headshot of the broker"></div>

    <div class="brand">
      <div class="brand-name">Marlowe Tessin</div>
      <div class="brand-tag">Real Estate</div>
    </div>

    <div class="agent">
      <div class="agent-name">Marlowe Tessin</div>
      <div class="agent-title">Broker</div>
    </div>

    <ul class="contact">
      <li><svg viewBox="0 0 10 10"><path d="M5 0a3.5 3.5 0 0 0-3.5 3.5C1.5 6 5 10 5 10s3.5-4 3.5-6.5A3.5 3.5 0 0 0 5 0zm0 5a1.4 1.4 0 1 1 0-2.8A1.4 1.4 0 0 1 5 5z" fill="var(--teal)"/></svg><span>782 W. Larkspur Ave, Suite 315<br>Cedar Grove, CA 91422</span></li>
      <li><svg viewBox="0 0 10 10"><path d="M2 0l2 2.5-1.2 1.3a6 6 0 0 0 3.4 3.4L7.5 6 10 8l-1.5 2C4 10 0 6 0 1.5z" fill="var(--teal)"/></svg><span>310-555-0148</span></li>
      <li><svg viewBox="0 0 10 10"><rect x="0" y="1.5" width="10" height="7" fill="var(--teal)"/><path d="M0 1.5l5 4 5-4" stroke="#fff" fill="none"/></svg><span>marlowe@marlowetessinrealestate.com</span></li>
      <li><svg viewBox="0 0 10 10"><circle cx="5" cy="5" r="4.2" fill="none" stroke="var(--teal)" stroke-width="1.4"/><path d="M1 5h8M5 1v8" stroke="var(--teal)"/></svg><span>www.marlowetessinrealestate.com</span></li>
    </ul>
  </section>

  <section class="card card-back" aria-label="Business card back">
    <h2 class="menu-title">MENU OF SERVICES</h2>
    <div class="services">
      <div class="service">
        <h3>Investor Services</h3>
        <ul><li>1% Listings for Flips</li><li>Rehab Management</li></ul>
      </div>
      <div class="service">
        <h3>Auction Services</h3>
        <ul><li>Bidding</li><li>Tax &amp; Title Review</li><li>Daily Auction Lists</li></ul>
      </div>
      <div class="service">
        <h3>Property Management</h3>
        <ul><li>Leasing</li><li>Maintenance</li><li>Evictions</li></ul>
      </div>
      <div class="service">
        <h3>Real Estate Services</h3>
        <ul><li>Buyers/Sellers</li><li>REO Specialists</li><li>BPO's</li><li>Notary</li></ul>
      </div>
    </div>
  </section>
</body>
</html>
```